Vale Crest Motors Business Card

Would like a cutting edge / high end Automotive Business card design. Please see current card which is old and dated. Would like to maintain the Vale Crest Motors logo and same information (address, website, etc).

See our website for the look and feel of what we offer - www.valecrestmotors.example

Target Market(s)

Upper class car buyers

Contact Information for Business Card

Modern high end business card design

Requirements
Nice to have
• Carbon Fiber look background

```html
<!DOCTYPE html>
<html lang="en">
<head>
<meta charset="utf-8">
<title>Vale Crest Motors Business Card</title>
<link rel="stylesheet" href="https://fonts.googleapis.com/css2?family=Poppins:wght@300;400;500;700&display=swap">
<style>
  :root {
    --backdrop: #2a2a2a;
    --card: #161616;
    --card-edge: #222222;
    --ink: #e8e8e8;
    --ink-soft: #bdbdbd;
    --icon-bg: #e2e2e2;
    --icon-ink: #1a1a1a;
  }
  * { margin: 0; padding: 0; box-sizing: border-box; }
  html, body { width: 1200px; height: 900px; overflow: hidden; }
  body {
    background: var(--backdrop);
    font-family: "Poppins", sans-serif;
    color: var(--ink);
  }
  .canvas {
    width: 1200px; height: 900px;
    display: flex; align-items: center; justify-content: center;
    gap: 90px;
  }
  .card {
    width: 360px; height: 620px;
    background: var(--card);
    border: 1px solid var(--card-edge);
    border-radius: 26px;
    display: flex; flex-direction: column; align-items: center;
    text-align: center;
    box-shadow: 0 20px 50px rgba(0,0,0,0.45);
  }
  .card--front { padding: 70px 30px 50px; }
  .card--back { justify-content: center; padding: 0 30px 80px; }

  .brand { display: flex; flex-direction: column; align-items: center; }
  .brand__name {
    font-weight: 500;
    color: var(--ink);
    letter-spacing: 0.06em;
    text-transform: uppercase;
    line-height: 1.1;
  }
  .brand__name--front { font-size: 34px; }
  .brand__name--back { font-size: 30px; }

  .tagline {
    margin-top: 18px;
    font-size: 11px;
    font-weight: 400;
    letter-spacing: 0.1em;
    color: var(--ink-soft);
    display: flex; align-items: center; gap: 12px;
  }
  .tagline__bar { width: 2px; height: 13px; background: var(--ink); }

  .person { margin-top: 54px; }
  .person__name { font-size: 28px; font-weight: 700; letter-spacing: 0.02em; }
  .person__role { font-size: 17px; font-weight: 300; letter-spacing: 0.06em; color: var(--ink-soft); }

  .icons { margin-top: 36px; display: flex; gap: 18px; }
  .icons__item {
    width: 26px; height: 26px; border-radius: 50%;
    background: var(--icon-bg);
    display: flex; align-items: center; justify-content: center;
  }
  .icons__item svg { width: 15px; height: 15px; }

  .contacts {
    margin-top: 34px;
    list-style: none;
    font-size: 16px; font-weight: 300;
    line-height: 1.85;
  }
  .contacts__web { font-weight: 300; }
  .contacts__web strong { font-weight: 500; }

  .divider { margin: 18px 0 16px; width: 22px; height: 3px; background: var(--ink); }

  .address { font-size: 16px; font-weight: 300; line-height: 1.5; font-style: normal; }

  .offer {
    margin-top: 20px;
    font-size: 17px; font-weight: 400; line-height: 1.3;
  }
</style>
</head>
<body>
<main class="canvas">
  <section class="card card--front" aria-label="Business card front">
    <div class="brand">
      <div class="brand__name brand__name--front">Vale Crest<br>Motors</div>
    </div>
    <div class="tagline">
      <span>QUALITY</span><span class="tagline__bar"></span>
      <span>INTEGRITY</span><span class="tagline__bar"></span>
      <span>SERVICE</span>
    </div>

    <div class="person">
      <div class="person__name">DANA MOREL</div>
      <div class="person__role">OWNER</div>
    </div>

    <div class="icons">
      <span class="icons__item" aria-label="Phone">
        <svg viewBox="0 0 16 16"><path fill="var(--icon-ink)" d="M3 6c0-2 1.5-3 5-3s5 1 5 3l-2.5 .5-.5-1.5h-4l-.5 1.5zM4 8h8l1 5H3z"/></svg>
      </span>
      <span class="icons__item" aria-label="Fax">
        <svg viewBox="0 0 16 16"><path fill="var(--icon-ink)" d="M4.5 2h7v3h-7zM2 6h12v6h-2.5V10h-7v2H2zM5.5 11h5v3h-5z"/></svg>
      </span>
      <span class="icons__item" aria-label="Email">
        <svg viewBox="0 0 16 16"><rect x="2" y="4" width="12" height="8" fill="var(--icon-ink)"/><path d="M2.5 4.5 8 9l5.5-4.5" stroke="var(--icon-bg)" stroke-width="1.2" fill="none"/></svg>
      </span>
      <span class="icons__item" aria-label="Website">
        <svg viewBox="0 0 16 16"><g fill="none" stroke="var(--icon-ink)" stroke-width="1.6"><rect x="6" y="1.5" width="4" height="7" rx="2" transform="rotate(20 8 5)"/><rect x="6" y="7.5" width="4" height="7" rx="2" transform="rotate(20 8 11)"/></g></svg>
      </span>
    </div>

    <ul class="contacts">
      <li>(555) 214-0387</li>
      <li>(555) 214-0392</li>
      <li>dana@valecrestmotors.example</li>
      <li class="contacts__web">www.<strong>valecrestmotors</strong>.example</li>
    </ul>

    <span class="divider"></span>

    <address class="address">1480 Harbor Ridge Road B<br>Marlow CA 90001</address>
  </section>

  <section class="card card--back" aria-label="Business card back">
    <div class="brand">
      <div class="brand__name brand__name--back">Vale Crest<br>Motors</div>
    </div>
    <p class="offer">Offering the Finest in<br>Luxury and Exotic<br>Sports Cars</p>
  </section>
</main>
</body>
</html>
```